Flyer-Design für regional agierendes Immobilienbüro
Zielgruppe
*regional agierendes Immobilienbüro
*Vermittlung von privaten Wohnimmobilien (Einfamilienhäuser, Wohnungen, Grundstücke)
*projektbezogene Zielgruppe: Immobilien Eigentümer / Verkäufer /Vermieter
*Idee: Gutschein über eine von drei Serviceleistungen - kostenlos*:
- Wertermittlung vom geprüften Preisbild-Berater
- Wohnflächen-Check
- Unterlagen-Check
*für Verkäufer / Vermieter im Wert von EUR 349,-
Aufgabenstellung
*CI (Style Guide, diverse Grafiken und Logos in verschiedenen Formaten vorhanden)
*cleanes, modernes Design - dennoch Eyecatcher (Postwurf)
*Ggf. DIN lang
Der Schlüssel zu einem erfolgreichen Verkauf liegt in der sorgfältigen Vorbereitung!
Passt der Verkaufspreis?
Sind alle Unterlagen vollständig und vorab auf mögliche 'Stolpersteine' geprüft?
Stimmt die Wohnfläche und sind alle Angaben rechtssicher korrekt?
Gerne prüfen wir, ob die grundlegenden Voraussetzungen für einen reibungslosen Verkauf Ihrer Immobilie zum bestmöglichen Verkaufspreis passen - kostenlos und unverbindlich! Im Rahmen eines unverbindlichen Beratungsgesprächs erfahren Sie auch, wie Sie von unserem vollumfänglichen Vermarktungsservice profitieren können.
Rufen Sie am besten gleich an und vereinbaren Sie einen Termin mit uns!

```html
<!DOCTYPE html>
<html lang="de">
<head>
<meta charset="utf-8">
<title>Gutschein-Flyer LINDHORST Immobilien</title>
<link href="https://fonts.googleapis.com/css2?family=Fira+Sans+Extra+Condensed:ital,wght@0,400;1,300;1,700;1,800&display=swap" rel="stylesheet">
<style>
:root{
  --page:#ffffff;
  --gold-light:#c9a26f;
  --gold-dark:#8d6d45;
  --gold-text:#c9a06a;
  --night:#050505;
  --petrol-light:#1a6c86;
  --petrol-dark:#0d4a60;
  --white:#ffffff;
  --cream:#f6efe5;
}
*{margin:0;padding:0;box-sizing:border-box}
html,body{width:849px;height:1200px;overflow:hidden;background:var(--page)}
body{position:relative;font-family:"Fira Sans Extra Condensed",sans-serif}
.flyer{
  position:absolute;left:222px;top:176px;width:404px;height:849px;
  box-shadow:2px 3px 6px rgba(0,0,0,.25);
}
.intro{
  position:absolute;left:0;top:0;width:404px;height:282px;padding:30px 0 0 20px;
  background:linear-gradient(110deg,var(--gold-light),var(--gold-dark));
  color:var(--cream);font-style:italic;font-weight:300;
  font-size:14.2px;line-height:20.5px;letter-spacing:-.2px;white-space:nowrap;
}
.intro p{margin-bottom:20.5px}
.intro .lead{font-weight:700;color:var(--white);letter-spacing:-.25px}
.photo{
  position:absolute;left:0;top:285px;width:404px;height:337px;
  background:radial-gradient(ellipse at 60% 35%,#d9dcdc 0%,#8f9696 35%,#2d3436 70%,#121617 100%);
}
.voucher{
  position:absolute;left:0;top:622px;width:404px;height:82px;background:var(--night);
}
.voucher-title{
  position:absolute;left:21px;top:18px;
  font-style:italic;font-weight:800;font-size:33px;line-height:40px;letter-spacing:-.2px;
  background:linear-gradient(180deg,#e0bb85,#a67e4c);
  -webkit-background-clip:text;background-clip:text;color:transparent;white-space:nowrap;
}
.voucher-list{
  position:absolute;left:238px;top:8px;list-style:none;
  font-style:italic;font-weight:700;font-size:16px;line-height:22px;color:var(--gold-text);white-space:nowrap;
}
.offer{
  position:absolute;left:0;top:707px;width:404px;height:81px;
  background:linear-gradient(110deg,var(--gold-light),var(--gold-dark));
  color:var(--white);text-align:center;font-style:italic;padding-top:12px;white-space:nowrap;
}
.offer-main{font-weight:700;font-size:15px;line-height:20.5px;letter-spacing:-.2px}
.offer-note{font-weight:300;font-size:11.5px;line-height:15px;color:var(--cream)}
.contact{
  position:absolute;left:0;top:790px;width:404px;height:59px;
  background:linear-gradient(180deg,var(--petrol-light),var(--petrol-dark));
  color:var(--white);text-align:center;font-size:15.5px;line-height:21px;padding-top:8px;white-space:nowrap;
}
.contact .sep{margin:0 4px}
</style>
</head>
<body>
<main class="flyer">
  <section class="intro">
    <p>Sind alle Unterlagen vollständig und vorab auf mögliche “Stolpersteine”<br>geprüft? Stimmt die Wohnfläche und sind alle Angaben rechtssicher?</p>
    <p class="lead">Gerne prüfen wir, ob die grundlegenden Voraussetzungen für<br>einen reibungslosen Verkauf Ihrer Immobilie zum bestmögli-<br>chen Verkaufs-preis passen - kostenlos und unverbindlich!</p>
    <p>Im Rahmen eines unverbindlichen Beratungsgesprächs erfahren Sie<br>auch, wie Sie von unserem vollumfänglichen Vermarktungsservice<br>profitieren können. Rufen Sie am besten gleich an und vereinbaren Sie<br>einen Termin mit uns - wir freuen uns auf Ihren Anruf!</p>
  </section>
  <div class="photo" role="img" aria-label="Foto: Hände mit Füllfederhalter über einem Übersichts- und Denkmalschutzplan auf einem Schreibtisch"></div>
  <section class="voucher">
    <h2 class="voucher-title">GUTSCHEIN ÜBER:</h2>
    <ul class="voucher-list">
      <li>- WERTERMITTLUNG</li>
      <li>- WOHNFLÄCHEN-CHECK</li>
      <li>- UNTERLAGEN-CHECK</li>
    </ul>
  </section>
  <section class="offer">
    <p class="offer-main">Mit diesem Gutschein erhalten Verkäufer / Vermieter eine der 3<br>oben genannten Serviceleistungen im Wert von 349 € kostenlos!</p>
    <p class="offer-note">Gültig bis 31.12.2018, keine Barauszahlung möglich.</p>
  </section>
  <footer class="contact">
    LINDHORST Immobilien<span class="sep">|</span>Jonas Berkhoff<span class="sep">|</span>Lindenallee 7<br>
    54321 Auenfeld<span class="sep">|</span>Telefon: 04321 98 76 540<span class="sep">|</span>www.lindhorst-immo.de
  </footer>
</main>
</body>
</html>
```